Men's Ministry Vesperine Church "Note to Clergy"

We need to update brochure line-up to the 21st Century. This piece will explain the value that a men's ministry affords a local parish. A majority of priests (male and female) do not know what the Kinsmen of St. Orwin can do to help them lay a solid foundation to grow, become more diversified, and present a positive picture for the local community
Updates

Under Must Not or avoid, please do not put the Kinsmen logo on the Front Panel, back shield reduce keep low key it. We need a 21st Century look that will appeal to Millennials, Gen-Xers, younger generation. Shield was created in 1883, it is about time we changed it.

Target Market(s)

Male and female clergy in the Hallowmere Vesperine Church

Industry/Entity Type

Non-Profit

Font styles to use
Serif

Requirements
Must have
• Slogan "Unleash the Orwin Within"
• Snappy enough to invite people to pick -up
Nice to have
• Want to keep Kinsmen of St. Orwin Logo on back panel, low keyed with address, web page and phone
Should not have
• political issues or political correctness

```html
<!DOCTYPE html>
<html lang="en">
<head>
<meta charset="utf-8">
<title>Unleash the Orwin Within – Trifold Brochure</title>
<link rel="stylesheet" href="https://fonts.googleapis.com/css2?family=Oswald:wght@500&family=Open+Sans:wght@400;600;700&display=swap">
<style>
  :root {
    --red: #e0141b;
    --red-deep: #c70f16;
    --blue: #2a1fa6;
    --ink: #161616;
    --white: #ffffff;
    --stage: #eeeeee;
    --sepia-light: #e6d8c2;
    --sepia-dark: #4a3526;
    --steel-light: #d8eef5;
    --steel-dark: #23343d;
  }
  * { box-sizing: border-box; margin: 0; padding: 0; }
  html, body { width: 1200px; height: 807px; overflow: hidden; }
  body {
    background: var(--stage);
    font-family: "Open Sans", Arial, sans-serif;
    display: flex; align-items: center; justify-content: center;
  }
  .brochure { display: flex; width: 1020px; height: 740px; box-shadow: 0 6px 24px rgba(0,0,0,.12); }
  .panel { position: relative; width: 340px; height: 740px; background: var(--white); overflow: hidden; }
  .panel svg.shapes { position: absolute; inset: 0; }

  /* Inside flap: ministry activities */
  .panel--activities { background: var(--red); }
  .activities {
    position: absolute; top: 30px; left: 24px; right: 20px;
    list-style: none; color: var(--white);
    font-size: 10.3px; line-height: 1.32;
  }
  .activities li { margin-bottom: 7px; }

  /* Back panel: contact */
  .crest {
    position: absolute; top: 318px; left: 0; right: 0;
    display: flex; align-items: center; justify-content: center; gap: 8px;
    color: var(--blue); font-weight: 600; font-size: 13px;
  }
  .crest__mark { width: 12px; height: 12px; background: var(--red); }
  .contact { position: absolute; top: 400px; left: 0; right: 0; text-align: center; }
  .contact__phone { font-weight: 700; font-size: 22px; color: var(--ink); letter-spacing: -0.3px; }
  .contact__email { font-size: 11.5px; color: var(--ink); margin-top: 6px; }
  .web {
    font-family: "Oswald", Arial, sans-serif; color: var(--red-deep);
    font-size: 13px; letter-spacing: 4.2px; margin-top: 14px;
  }

  /* Front cover */
  .slogan {
    position: absolute; top: 545px; left: 0; right: 0; text-align: center;
    font-family: "Oswald", Arial, sans-serif; font-weight: 500; line-height: 1.05;
  }
  .slogan__lead { color: var(--red-deep); font-size: 44px; display: block; }
  .slogan__tail { color: var(--ink); font-size: 44px; display: block; }
  .cover-web { position: absolute; top: 660px; left: 0; right: 0; text-align: center; margin: 0; }
</style>
</head>
<body>
<main class="brochure">

  <section class="panel panel--activities">
    <svg class="shapes" width="340" height="740" viewBox="0 0 340 740">
      <defs>
        <radialGradient id="crossLight" cx="0.45" cy="0.4" r="0.8">
          <stop offset="0" stop-color="var(--steel-light)"/>
          <stop offset="1" stop-color="var(--steel-dark)"/>
        </radialGradient>
      </defs>
      <path d="M140 740 C210 680 290 640 340 628 L340 740 Z" fill="var(--blue)"/>
      <path d="M0 650 C120 638 240 618 340 598 L340 632 C280 645 210 685 150 740 L0 740 Z" fill="var(--white)"/>
      <path d="M0 664 C110 654 220 636 300 618 C230 652 175 692 130 740 L0 740 Z" fill="url(#crossLight)" role="img" aria-label="Photo: a cross glowing with rays of light above a crowd"/>
    </svg>
    <ul class="activities">
      <li>Voluntary donation to the Vesperine Community of Ministry for Men through the Kinsmen of St. Orwin supports the following activities benefiting local parishes:</li>
      <li>Building Partnerships and Alliances to gain resources plus state of the art facilitating, mentoring, and/or leadership training for expanding Congregational Vitality.</li>
      <li>Providing Web Page, social media, blog, and video channels capabilities for idea sharing, inquiries, and testimonials.</li>
      <li>Special event planning for local parish, deanery, or parish use during a ministry fair day atmosphere.</li>
      <li>Assisting Parishes and Dioceses in creating Men's Ministry links and formats to disciple men to Christ.</li>
      <li>Primary resource and clearing house for Restorative Justice Ministry program opportunities including: Open Door, Veteran's Courts, Half-Way Houses, In Prison Kinsmen ministry, Step-Houses, and Summer Camps for the children of incarcerated men.</li>
      <li>Facilitating local parishes develop Veteran Friendly Congregations to provide a safe haven for veterans encountering post dramatic stress disorder, addictions, suicidal tendencies, spouse abuse, and divorces.</li>
      <li>Helping young men develop spirituality through participating in Trailway Scouts activities.</li>
      <li>Mentoring programs for the inner city fatherless young men.</li>
      <li>Supporting Vesperine Community Service programs to combat homelessness; participating in such programs as Hearth for Neighbors.</li>
    </ul>
  </section>

  <section class="panel panel--contact">
    <svg class="shapes" width="340" height="740" viewBox="0 0 340 740">
      <defs>
        <linearGradient id="sunsetCrowd" x1="0" y1="0" x2="0.4" y2="1">
          <stop offset="0" stop-color="var(--sepia-light)"/>
          <stop offset="1" stop-color="var(--sepia-dark)"/>
        </linearGradient>
      </defs>
      <path d="M0 0 C40 120 180 210 340 265 L340 282 C170 230 30 140 0 30 Z" fill="var(--blue)"/>
      <path d="M10 0 C50 110 190 200 340 250 L340 265 C180 210 40 120 0 10 Z" fill="var(--red)"/>
      <path d="M22 0 H340 V248 C195 198 60 110 22 0 Z" fill="url(#sunsetCrowd)" role="img" aria-label="Photo: silhouettes of people raising their arms before a large cross at sunrise"/>
      <path d="M0 690 C120 680 250 640 340 590 L340 740 L0 740 Z" fill="var(--blue)"/>
    </svg>
    <div class="crest"><span class="crest__mark"></span>Kinsmen of St. Orwin</div>
    <div class="contact">
      <p class="contact__phone">CALL US : (555) 014-2290</p>
      <p class="contact__email">kinsmenofstorwin@kinsmenorwin.net</p>
      <p class="web">www.kinsmenorwin.net</p>
    </div>
  </section>

  <section class="panel panel--cover">
    <svg class="shapes" width="340" height="740" viewBox="0 0 340 740">
      <defs>
        <linearGradient id="sunsetFamily" x1="0.5" y1="0" x2="0.3" y2="1">
          <stop offset="0" stop-color="var(--sepia-light)"/>
          <stop offset="1" stop-color="var(--sepia-dark)"/>
        </linearGradient>
      </defs>
      <path d="M0 440 L200 520 L340 410 L340 430 L200 535 L0 455 Z" fill="var(--blue)"/>
      <path d="M0 428 L200 508 L340 396 L340 412 L200 522 L0 442 Z" fill="var(--red)"/>
      <path d="M0 0 H340 V392 L200 500 L0 422 Z" fill="url(#sunsetFamily)" role="img" aria-label="Photo: a family in silhouette holding hands with arms raised beneath a glowing cross"/>
      <rect x="0" y="680" width="340" height="60" fill="var(--blue)"/>
    </svg>
    <h1 class="slogan">
      <span class="slogan__lead">Unleash the</span>
      <span class="slogan__tail">Orwin Within</span>
    </h1>
    <p class="web cover-web">www.kinsmenorwin.net</p>
  </section>

</main>
</body>
</html>
```